" A Quitavel é uma empresa que desenvolve e fornece o sistema de cobrança Quitavel para empresas de cobrança (escritórios de cobrança, assessorias de cobranças, escritórios de advogados), tais clientes chamamos de ASSESSORIAS, e também fornecemos o sistema para empresas que possuem uma grande quantidade de clientes inadimplentes e que fazem a cobrança destes clientes internamente através de um departamento de cobrança, estes clientes chamamos de CREDORES. Alguns clientes ASSESSORIAS: www.grupoltn-exemplo.com.br www.moraisetavares-exemplo.com.br www.rvrecupera-exemplo.com.br Alguns clientes CREDORES: www.linguaviva-exemplo.com www.grupovelarium-exemplo.com.br www.ronaldos-exemplo.com.br Todos os produtos e serviços que comercializamos são através da plataforma Quitavel, por exemplo, para que um cliente utilize nosso produto “Portal de Negociação” ele precisa contratar o Quitavel já que suas configurações são através do sistema, da mesma forma o serviço de “SMS”, já que as campanhas são criadas e disparadas pelo sistema Quitavel. O sistema Quitavel “nasceu” primeiro que a empresa Quitavel, já que dois dos atuais sócios possuíram uma empresa anterior de 2012 até a abertura da Quitavel em 1 de setembro de 2015. Esta empresa desenvolvia um sistema focado para assessorias de cobrança, porém em uma tecnologia antiga, e então resolveram criar um novo software com tecnologias atuais na época e para isto buscaram um investidor e juntos optaram por criar uma nova empresa, uma nova marca. Nossa logo foi construída através da plataforma Marca Pronta e gostamos muito do resultado! E estamos aqui novamente buscando que seus profissionais nos ajudem a criar novos materiais que hoje se fazem necessários para nós. "

```html
<!DOCTYPE html>
<html lang="pt-BR">
<head>
<meta charset="utf-8">
<title>Título da Apresentação — Quitavel</title>
<link rel="stylesheet" href="https://fonts.googleapis.com/css2?family=Fira+Sans+Condensed:wght@600;700&family=Fira+Sans:wght@400;600;700&display=swap">
<style>
  :root {
    --brand-blue: #0e3a8e;
    --heading-blue: #184a9c;
    --panel-tint: #dcedf1;
    --body-grey: #5b6470;
    --rule-grey: #b9ccd6;
    --white: #ffffff;
    --art-light: #f3c98b;
    --art-dark: #a9d3e6;
  }
  * { margin: 0; padding: 0; box-sizing: border-box; }
  html, body { width: 1200px; height: 1200px; overflow: hidden; background: var(--white); }
  .slide { position: relative; width: 1200px; height: 1200px; background: var(--white); font-family: "Fira Sans", sans-serif; }

  .title-band {
    position: absolute; left: 0; top: 139px; width: 1200px; height: 185px;
    background: var(--brand-blue);
    display: flex; align-items: center; padding-left: 228px;
  }
  .title-band h1 {
    font-family: "Fira Sans Condensed", sans-serif; font-weight: 700;
    font-size: 77px; color: var(--white); letter-spacing: 0.3px;
  }

  .content-panel {
    position: absolute; left: 0; top: 324px; width: 1200px; height: 595px;
    background: var(--panel-tint);
  }
  .hero-art {
    position: absolute; left: 108px; top: 108px; width: 456px; height: 360px;
    border-radius: 24px;
    background: radial-gradient(circle at 50% 70%, var(--art-light) 0%, var(--art-light) 22%, var(--art-dark) 60%, var(--panel-tint) 100%);
  }
  .pitch { position: absolute; left: 593px; top: 176px; width: 550px; }
  .pitch h2 {
    font-weight: 700; font-size: 29px; line-height: 1.25; color: var(--heading-blue);
  }
  .pitch p {
    margin-top: 38px; font-size: 22px; line-height: 1.35; color: var(--body-grey);
    border-left: 2px solid var(--rule-grey); padding-left: 10px;
  }

  .footer-band {
    position: absolute; left: 0; top: 919px; width: 1200px; height: 113px;
    background: var(--brand-blue);
  }
  .brand {
    position: absolute; left: 80px; top: 0; height: 113px;
    display: flex; align-items: center;
    color: var(--white); font-weight: 700; font-size: 64px; line-height: 1; letter-spacing: -1px;
  }
  .site-box {
    position: absolute; left: 396px; top: 41px; width: 780px; height: 60px;
    background: var(--white);
    display: flex; align-items: center; justify-content: center;
  }
  .site-box span { font-weight: 700; font-size: 30px; color: var(--brand-blue); letter-spacing: 0.3px; }
</style>
</head>
<body>
<main class="slide">
  <header class="title-band">
    <h1>Título da Apresentação</h1>
  </header>

  <section class="content-panel">
    <div class="hero-art" role="img" aria-label="Ilustração de atendente com headset ao computador, cercado por ícones de SMS, e-mail, suporte, nuvem e dinheiro"></div>
    <div class="pitch">
      <h2>Plataforma simples e eficiente para sua cobrança ter mais resultados</h2>
      <p>O Quitavel é um sistema de cobrança que irá simplificar a operação e gestão de suas cobranças.</p>
    </div>
  </section>

  <footer class="footer-band">
    <div class="brand">Quitavel</div>
    <div class="site-box"><span>ACESSE: WWW.QUITAVEL-EXEMPLO.COM.BR</span></div>
  </footer>
</main>
</body>
</html>
```